Dietitian clinic needs a business card design

We need a business card design for a new dietitian group based in Singapore called "Lantern and Tide". We provide expert, personalised nutrition care to support a wide range of health needs, from chronic conditions to mindful eating. Our team also offers consulting, speaking, and tailored solutions for healthcare providers, organisations, and food services.

Target Market(s)

Adults

Industry/Entity Type

Healthcare

Contact Information for Business Card

Name, position, contact number, email, website address, our logo

Requirements
Nice to have
• Clean, professional but welcoming look

```html
<!DOCTYPE html>
<html lang="en">
<head>
<meta charset="utf-8">
<title>Lantern and Tide — Business Card</title>
<link href="https://fonts.googleapis.com/css2?family=DM+Serif+Display&family=Open+Sans:wght@400;600&display=swap" rel="stylesheet">
<style>
  :root{
    --page-bg:#1b1c1e;
    --card-teal:#1f5b6c;
    --card-teal-deep:#1c4a64;
    --card-edge:#e7a2a2;
    --accent-pink:#eaa9a8;
    --text-light:#f3f5f6;
    --divider:rgba(243,245,246,.75);
  }
  *{box-sizing:border-box;margin:0;padding:0}
  html,body{width:1200px;height:840px;overflow:hidden}
  body{
    background:var(--page-bg);
    display:flex;align-items:center;justify-content:center;gap:40px;
    font-family:"Open Sans",Arial,sans-serif;
  }
  .card{
    position:relative;
    width:540px;height:310px;
    border-radius:22px;
    background:radial-gradient(ellipse at 45% 60%,var(--card-teal-deep) 0%,var(--card-teal) 70%);
    border:2px solid var(--card-edge);
    box-shadow:0 4px 0 var(--card-edge);
    overflow:hidden;
  }
  /* front */
  .card-front{display:flex;align-items:center;justify-content:center;gap:16px}
  .front-dot{width:22px;height:22px;border-radius:50%;background:var(--accent-pink)}
  .front-name{
    font-family:"DM Serif Display",Georgia,serif;
    font-size:46px;line-height:1;color:var(--accent-pink);letter-spacing:.5px;
  }
  /* back */
  .brand{
    position:absolute;top:34px;right:40px;
    display:flex;align-items:center;gap:14px;
  }
  .brand-dot{width:18px;height:18px;border-radius:50%;background:var(--accent-pink)}
  .brand-name{
    font-family:"DM Serif Display",Georgia,serif;
    font-size:40px;line-height:.9;color:var(--accent-pink);
  }
  .brand-name span{display:block;padding-left:44px}
  .details{
    position:absolute;top:150px;left:0;right:0;
    display:flex;justify-content:center;align-items:center;
  }
  .person{text-align:right;padding-right:16px}
  .person-name{
    font-family:"DM Serif Display",Georgia,serif;
    font-size:22px;letter-spacing:1px;color:var(--accent-pink);text-transform:uppercase;line-height:1.1;
  }
  .person-role{font-size:15px;color:var(--text-light);margin-top:2px}
  .divider{width:1px;height:78px;background:var(--divider)}
  .contact{list-style:none;padding-left:16px}
  .contact li{display:flex;align-items:center;gap:7px;font-size:14px;color:var(--text-light);line-height:1.6}
  .contact svg{width:12px;height:12px;flex:none}
  .address{
    position:absolute;bottom:34px;left:0;right:0;text-align:center;
    font-size:15px;color:var(--text-light);letter-spacing:.2px;
  }
</style>
</head>
<body>

  <section class="card card-front" aria-label="Card front">
    <div class="front-dot"></div>
    <div class="front-name">lantern &amp; tide</div>
  </section>

  <section class="card card-back" aria-label="Card back">
    <div class="brand">
      <div class="brand-dot"></div>
      <div class="brand-name">lantern<span>&amp;tide</span></div>
    </div>

    <div class="details">
      <div class="person">
        <div class="person-name">Mara Linwood</div>
        <div class="person-role">Managing Director</div>
      </div>
      <div class="divider"></div>
      <ul class="contact">
        <li>
          <svg viewBox="0 0 12 12" aria-hidden="true"><path fill="#eaa9a8" d="M2.5 1h2l1 2.5-1.3 1a6 6 0 0 0 3.3 3.3l1-1.3L11 7.5v2A1.5 1.5 0 0 1 9.5 11 8.5 8.5 0 0 1 1 2.5 1.5 1.5 0 0 1 2.5 1z"/></svg>
          065-310 482 907
        </li>
        <li>
          <svg viewBox="0 0 12 12" aria-hidden="true"><rect x="1" y="2.5" width="10" height="7" rx="1" fill="#eaa9a8"/><path d="M1.5 3l4.5 3.5L10.5 3" stroke="#1f5b6c" stroke-width="1" fill="none"/></svg>
          hello@lanternandtide.sg
        </li>
        <li>
          <svg viewBox="0 0 12 12" aria-hidden="true"><circle cx="6" cy="6" r="5" fill="#eaa9a8"/><path d="M1 6h10M6 1c2 2 2 8 0 10M6 1c-2 2-2 8 0 10" stroke="#1f5b6c" stroke-width=".8" fill="none"/></svg>
          www.lanternandtide.sg
        </li>
      </ul>
    </div>

    <div class="address">Your Address, City, State, Zip 0000</div>
  </section>

</body>
</html>
```